Printing company needs a presentational catalogue, min. A5 format when closed, portrait or landscape

We need a corporate catalogue design for presentation of our company/services mainly to corporate customers. Our portfolio of services includes: offset printing, digital printing, screen printing, UV flatbed printing, direct UV printing on promotional items, textile printing (direct screen printing and heat transfer), computer cutting/plotting, CNC cutting, graphic design, setting for press; You can also use images of our products from our website www.lastovkabarve.si
We will adopt text later to the design so there should be some free space left for text. You should also determinate the typography of fonts for the category titles (offset printing, digital printing, etc...) and description of individual category.
Design should communicate in a way that we are there to solve our customer´s graphic problems and needs. Our new logo is attached. Catalogue colours should be matched with our new logo (kobalt lini). We will change our website soon (from lastovkabarve to kobaltlini), so the catalogue should not be in colours of existent website design (blue and orange).

Target Market(s)

B2B customers (mixed field of work)

Industry/Entity Type

Printing

Requirements
Must have
• Our new company logo, but it should not step out too much (better to be small and discreet).
Nice to have
• Some images of products that we offer - they could be from our website www.lastovkabarve.si if you can integrate them well into design...

```html
<!DOCTYPE html>
<html lang="sl">
<head>
<meta charset="utf-8">
<title>Kobalt lini – katalog, naslovnica</title>
<link rel="stylesheet" href="https://fonts.googleapis.com/css2?family=Montserrat:wght@500&display=swap">
<style>
  :root {
    --stage-top: #8c8c8c;
    --stage-bottom: #f2f2f2;
    --cover: #ffffff;
    --brand-red: #d7262e;
    --brand-blue: #2c5f97;
    --ink: #3a3a3a;
  }
  * { margin: 0; padding: 0; box-sizing: border-box; }
  html, body { width: 1200px; height: 936px; overflow: hidden; }
  body {
    background: linear-gradient(180deg, var(--stage-top) 0%, #c9c9c9 45%, var(--stage-bottom) 100%);
    display: flex;
    align-items: center;
    justify-content: center;
    font-family: "Montserrat", Arial, sans-serif;
  }
  .cover {
    position: relative;
    width: 580px;
    height: 820px;
    background: var(--cover);
    box-shadow: 0 18px 40px rgba(0,0,0,.18);
  }
  .brand {
    position: absolute;
    top: 68px;
    right: 46px;
    display: flex;
    align-items: center;
    gap: 12px;
  }
  .brand-mark {
    width: 30px;
    height: 30px;
    background: var(--brand-red);
    border-radius: 3px;
  }
  .brand-name {
    font-size: 24px;
    font-weight: 500;
    color: var(--ink);
    letter-spacing: .01em;
    text-transform: uppercase;
  }
  .service-strip {
    position: absolute;
    left: 0;
    right: 0;
    bottom: 0;
    height: 240px;
    display: grid;
    grid-template-columns: repeat(6, 1fr);
    gap: 2px;
    background: var(--cover);
  }
  .service {
    display: flex;
    flex-direction: column;
  }
  .service-band {
    height: 14px;
    background: var(--brand-blue);
  }
  .service-band.is-accent { background: var(--brand-red); }
  .service-image { flex: 1; margin-top: 2px; }
  .img-press    { background: linear-gradient(180deg, #d9dde0 0%, #b8bfc4 50%, #b52a2a 75%, #8e1f1f 100%); }
  .img-paper    { background: linear-gradient(160deg, #f2f2f2 0%, #9a9fa4 45%, #e8e8e8 100%); }
  .img-film     { background: linear-gradient(150deg, #9ec9ec 0%, #3f86c9 40%, #1b3d66 70%, #0c1220 100%); }
  .img-textile  { background: linear-gradient(180deg, #5a7594 0%, #3d5a7c 60%, #4a6686 100%); }
  .img-promo    { background: linear-gradient(180deg, #f7f7f7 0%, #d8cbb8 45%, #efefef 100%); }
  .img-building { background: linear-gradient(180deg, #e6e8e8 0%, #c8c4bb 55%, #a9a195 100%); }
</style>
</head>
<body>
  <main class="cover">
    <header class="brand">
      <span class="brand-mark" aria-hidden="true"></span>
      <span class="brand-name">kobalt lini</span>
    </header>

    <section class="service-strip" aria-label="Storitve">
      <div class="service">
        <div class="service-band"></div>
        <div class="service-image img-press" role="img" aria-label="Offsetni tiskarski stroj"></div>
      </div>
      <div class="service">
        <div class="service-band"></div>
        <div class="service-image img-paper" role="img" aria-label="Listi tiskanega papirja"></div>
      </div>
      <div class="service">
        <div class="service-band"></div>
        <div class="service-image img-film" role="img" aria-label="Modre folije za digitalni tisk"></div>
      </div>
      <div class="service">
        <div class="service-band"></div>
        <div class="service-image img-textile" role="img" aria-label="Potisk na tekstil, blago z napisom"></div>
      </div>
      <div class="service">
        <div class="service-band is-accent"></div>
        <div class="service-image img-promo" role="img" aria-label="UV tisk na promocijske izdelke"></div>
      </div>
      <div class="service">
        <div class="service-band"></div>
        <div class="service-image img-building" role="img" aria-label="Velikoformatni tisk na fasadi stavbe"></div>
      </div>
    </section>
  </main>
</body>
</html>
```